Business Card for Bright Meadow Lawn & Landscape

Double Sided Card Design - I think one side of the card should be cleaner, with logo, contact info, and "Complete Residential & Commercial Landscape Services", and on the other side it should list the services we offer:

- Lawn Care & Mowing
- Hedge & Shrub Trimming
- Leaf Removal & Clean Up
- Aeration & Sod
- Mulch & Rock Installations
- Landscape Installations & Renovations
- Commercial Snow Removal

Please make it clean and very professional... don't want it too be too busy, but want to tell them what we do.

Target Market(s)

Residential and Commercial

Industry/Entity Type

Landscape

Contact Information for Business Card

Fully Insured
Tom Berrigan
410-555-0198
Tberrigan07@mailbox-example.com

Requirements
Must have
• Double Sided, Cleaner on one side, more information and text on the other side.

```html
<!DOCTYPE html>
<html lang="en">
<head>
<meta charset="utf-8">
<title>Bright Meadow Lawn &amp; Landscape – Business Card</title>
<link rel="stylesheet" href="https://fonts.googleapis.com/css2?family=Roboto:wght@400;500;700&family=Roboto+Condensed:wght@400;700&display=swap">
<style>
  :root {
    --bg: #2b2b2b;
    --green: #8ab800;
    --black: #030303;
    --white: #ffffff;
  }
  html, body {
    margin: 0;
    width: 1200px;
    height: 960px;
    overflow: hidden;
    background: var(--bg);
    font-family: "Roboto", sans-serif;
  }
  .canvas {
    position: relative;
    width: 1200px;
    height: 960px;
  }
  .card {
    position: absolute;
    left: 320px;
    width: 600px;
    height: 340px;
    border-radius: 16px;
    overflow: hidden;
  }
  /* Services side */
  .card-front {
    top: 108px;
    background: var(--green);
    color: var(--white);
  }
  .front-brand {
    position: absolute;
    top: 100px;
    left: 0;
    width: 100%;
    text-align: center;
    font-family: "Roboto", sans-serif;
    font-weight: 500;
    font-size: 34px;
    letter-spacing: 1px;
    color: var(--white);
  }
  .services {
    position: absolute;
    top: 248px;
    left: 0;
    width: 100%;
    margin: 0;
    text-align: center;
    font-size: 14.5px;
    line-height: 19px;
  }
  .services .dot { padding: 0 3px; }

  /* Contact side */
  .card-back {
    top: 495px;
    background: var(--black);
    color: var(--white);
  }
  .wave {
    position: absolute;
    inset: 0;
  }
  .brand {
    position: absolute;
    top: 38px;
    left: 330px;
    width: 240px;
    text-align: center;
    color: var(--green);
    font-family: "Roboto", sans-serif;
    font-weight: 500;
  }
  .brand-mark {
    width: 72px;
    height: 72px;
    margin: 0 auto 10px;
    border-radius: 50%;
    background: var(--green);
  }
  .brand-name {
    font-size: 25px;
    line-height: 26px;
    letter-spacing: 0.5px;
  }
  .brand-tag {
    font-size: 13px;
    letter-spacing: 2.5px;
    text-transform: uppercase;
  }
  .contact {
    position: absolute;
    left: 32px;
    top: 180px;
    font-family: "Roboto Condensed", sans-serif;
  }
  .insured {
    font-size: 21px;
    font-weight: 700;
    line-height: 24px;
    text-transform: uppercase;
  }
  .person {
    font-family: "Roboto", sans-serif;
    font-size: 18px;
    font-weight: 500;
    line-height: 22px;
    text-transform: uppercase;
    margin-bottom: 10px;
  }
  .line {
    display: flex;
    align-items: center;
    gap: 8px;
    font-family: "Roboto", sans-serif;
    font-size: 14.5px;
    line-height: 19px;
  }
  .line svg { flex: none; }
  .tagline {
    margin-top: 8px;
    font-size: 16px;
    line-height: 19px;
  }
</style>
</head>
<body>
<main class="canvas">
  <section class="card card-front" aria-label="Services side">
    <div class="front-brand">Bright Meadow</div>
    <p class="services">
      Lawn Care &amp; Mowing<span class="dot">•</span>Hedge &amp; Shrub Trimming<br>
      Leaf Removal &amp; Clean Up<span class="dot">•</span>Aeration &amp; Sod<span class="dot">•</span>Mulch &amp; Rock Installations<br>
      Landscape Installations &amp; Renovations<span class="dot">•</span>Commercial Snow Removal
    </p>
  </section>

  <section class="card card-back" aria-label="Contact side">
    <svg class="wave" width="600" height="340" viewBox="0 0 600 340" aria-hidden="true">
      <path fill="var(--green)" d="M0,160 C60,115 150,120 260,185 C380,255 480,300 600,305 L600,340 L0,340 Z"/>
      <path fill="var(--white)" d="M20,132 C150,110 300,210 400,265 C480,305 550,318 600,318 L600,336 C540,336 470,320 390,282 C290,232 160,128 20,132 Z"/>
    </svg>

    <div class="brand">
      <div class="brand-mark"></div>
      <div class="brand-name">Bright Meadow</div>
      <div class="brand-tag">Lawn &amp; Landscape</div>
    </div>

    <div class="contact">
      <div class="insured">Fully Insured</div>
      <div class="person">Tom Berrigan</div>
      <div class="line">
        <svg width="12" height="16" viewBox="0 0 12 16" aria-hidden="true"><rect x="1" y="1" width="10" height="14" rx="2" fill="none" stroke="#fff" stroke-width="2"/><rect x="4" y="12" width="4" height="1.5" fill="#fff"/></svg>
        <span>410-555-0198</span>
      </div>
      <div class="line">
        <svg width="12" height="10" viewBox="0 0 12 10" aria-hidden="true"><rect x="0" y="1" width="12" height="8" fill="#fff"/><path d="M0,1 L6,6 L12,1" fill="none" stroke="var(--green)" stroke-width="1.2"/></svg>
        <span>Tberrigan07@mailbox-example.com</span>
      </div>
      <div class="tagline">Complete Residential<br>Commercial Landscape Services</div>
    </div>
  </section>
</main>
</body>
</html>
```